martial arts school needs a flyer to attract new starters in wing chun kung fu

we need a flyer design to be sent out in the local community to attract new customers to our martial arts school. we intend to run introduction classes for begineers. the design should be attractive to new starters looking to get fit - learn a martial art - make new friends - improve self confidence.
also the flyer should say "free class with this flyer" . we also need big poster to put up around the local area

the following dress should be on the design Aire Valley Martial ArtsGround FloorThe MillGreengage RoadKeighleyBD21 5LH Added Sunday, April 5, 2015

contact telephone number on the design ; 079 64820 557 Added Sunday, April 5, 2015

• it must say - wing chun kung fu classes - introduction classes -

```html
<!DOCTYPE html>
<html lang="en">
<head>
<meta charset="utf-8">
<title>Wing Chun Kung Fu Classes – Flyer</title>
<link href="https://fonts.googleapis.com/css2?family=Anton&family=Bebas+Neue&family=Roboto:wght@400;700;900&display=swap" rel="stylesheet">
<style>
  :root {
    --backdrop: #ffffff;
    --ink: #111111;
    --navy: #142a4c;
    --navy-deep: #0d1533;
    --grey-light: #e9e9e9;
    --grey-mid: #b9b9b9;
    --grey-dark: #4a4a4a;
    --photo-light: #f6f6f6;
    --photo-mid: #dcdcdc;
    --photo-shade: #c4c4c4;
    --offer-yellow: #fff200;
    --offer-red: #e2131b;
    --white: #ffffff;
  }
  * { box-sizing: border-box; margin: 0; padding: 0; }
  html, body { width: 1200px; height: 1000px; overflow: hidden; background: var(--backdrop); }
  .canvas { position: relative; width: 1200px; height: 1000px; }

  .flyer {
    position: absolute; left: 290px; top: 60px;
    width: 620px; height: 880px;
    background: var(--white);
    border: 2px solid var(--ink);
    overflow: hidden;
  }

  .title-band {
    position: absolute; left: 0; top: 0; width: 100%; height: 102px;
    background: linear-gradient(to bottom, var(--grey-mid) 0%, #dcdcdc 30%, var(--grey-light) 100%);
    display: flex; align-items: flex-end; justify-content: center;
    padding-bottom: 14px;
  }
  .title {
    font-family: "Anton", "Impact", sans-serif;
    font-size: 40px; letter-spacing: 1.5px; color: var(--ink);
    line-height: 1;
  }

  .intro-band {
    position: absolute; left: 0; top: 102px; width: 100%; height: 110px;
    background: linear-gradient(to bottom, #f4f4f4, #e2e2e2);
    clip-path: polygon(0 0, 100% 0, 100% 72%, 0 100%);
  }
  .intro-rule { position: absolute; left: 0; top: 102px; width: 620px; height: 112px; }

  .school-mark {
    position: absolute; left: 16px; top: 124px;
    display: flex; align-items: center; gap: 6px;
  }
  .school-mark__dot {
    width: 60px; height: 60px; border-radius: 50%;
    background: var(--grey-dark);
  }
  .school-mark__name {
    width: 82px;
    font-family: "Roboto", Arial, sans-serif; font-weight: 700;
    font-size: 11px; line-height: 1.25; color: var(--grey-dark);
    text-transform: uppercase;
  }

  .intro-heading {
    position: absolute; left: 176px; top: 130px;
    font-family: "Roboto", Arial, sans-serif; font-weight: 700;
    font-size: 27px; line-height: 1.05; letter-spacing: 3.5px; color: var(--ink);
  }

  .watermark-ring {
    position: absolute; left: 40px; top: 200px; width: 520px; height: 520px;
    border-radius: 50%; border: 36px solid rgba(0,0,0,0.04);
  }

  .student-photo {
    position: absolute; left: 330px; top: 168px; width: 290px; height: 470px;
    background: radial-gradient(ellipse 70% 60% at 60% 62%, var(--photo-light) 0%, var(--photo-mid) 60%, var(--photo-shade) 100%);
    -webkit-mask-image: linear-gradient(to right, transparent 0%, #000 22%);
            mask-image: linear-gradient(to right, transparent 0%, #000 22%);
    opacity: 0.85;
  }

  .benefits {
    position: absolute; left: 26px; top: 412px;
    list-style: none;
    font-family: "Bebas Neue", "Oswald", sans-serif;
    font-size: 52px; line-height: 47px; color: var(--navy);
  }
  .benefits li:nth-child(3), .benefits li:nth-child(4) { color: var(--navy-deep); }

  .base-shape { position: absolute; left: 0; top: 530px; width: 620px; height: 350px; }

  .contact {
    position: absolute; left: 0; top: 698px; width: 100%;
    text-align: center; color: var(--white);
    font-family: "Roboto", Arial, sans-serif;
  }
  .contact__phone {
    display: flex; align-items: center; justify-content: center; gap: 16px;
    font-weight: 700; font-size: 48px; line-height: 1; letter-spacing: 1px;
  }
  .contact__phone svg { width: 54px; height: 40px; }
  .contact__address { margin-top: 14px; font-size: 19px; line-height: 1.18; }

  .offer {
    position: absolute; left: 0; bottom: 0; width: 100%; height: 62px;
    background: var(--offer-yellow);
    display: flex; align-items: center; justify-content: center;
    font-family: "Roboto", Arial, sans-serif; font-weight: 900;
    font-size: 27px; color: var(--offer-red);
  }
</style>
</head>
<body>
<main class="canvas">
  <article class="flyer">
    <header class="title-band">
      <h1 class="title">WING CHUN KUNG FU CLASSES</h1>
    </header>

    <div class="intro-band"></div>
    <svg class="intro-rule" viewBox="0 0 620 112" aria-hidden="true">
      <line x1="0" y1="110" x2="620" y2="80" stroke="#9a9a9a" stroke-width="3"/>
    </svg>

    <div class="watermark-ring" aria-hidden="true"></div>

    <div class="school-mark">
      <span class="school-mark__dot" aria-hidden="true"></span>
      <span class="school-mark__name">Brook Hollow Martial Arts</span>
    </div>

    <h2 class="intro-heading">INTRODUCTION<br>CLASSES</h2>

    <div class="student-photo" role="img" aria-label="Photo of a smiling male student in a white martial arts uniform with arms folded"></div>

    <ul class="benefits">
      <li>Get Fit</li>
      <li>Make New Friends</li>
      <li>Learn a Martial Art</li>
      <li>Improve Self-Confidence</li>
    </ul>

    <svg class="base-shape" viewBox="0 0 620 350" preserveAspectRatio="none" aria-hidden="true">
      <defs>
        <linearGradient id="panelShade" x1="0" y1="0" x2="0" y2="1">
          <stop offset="0" stop-color="#5a5a5a"/>
          <stop offset="0.3" stop-color="#1e1e1e"/>
          <stop offset="1" stop-color="#050505"/>
        </linearGradient>
      </defs>
      <path d="M0 122 C 220 118, 440 78, 620 0 L620 350 L0 350 Z" fill="#142a4c"/>
      <path d="M0 138 C 235 134, 450 92, 620 16 L620 350 L0 350 Z" fill="#0d1533"/>
      <path d="M0 155 C 250 150, 460 108, 620 36 L620 350 L0 350 Z" fill="url(#panelShade)"/>
    </svg>

    <section class="contact">
      <p class="contact__phone">
        <svg viewBox="0 0 54 40" aria-hidden="true">
          <path d="M4 14 C4 4 50 4 50 14 L50 18 L38 18 L38 12 L16 12 L16 18 L4 18 Z" fill="#ffffff"/>
          <path d="M14 20 L40 20 L48 38 L6 38 Z" fill="#ffffff"/>
          <circle cx="27" cy="29" r="5" fill="#1e1e1e"/>
        </svg>
        079 64820 557
      </p>
      <p class="contact__address">Brook Hollow Martial Arts Ground Floor<br>The Tannery Spindlewick Road Marlowick TQ47 9RX</p>
    </section>

    <footer class="offer">Bring this flyer in for a FREE WEEK!</footer>
  </article>
</main>
</body>
</html>
```